USA Home and Kitchen "Multi-Product" Brand Needs a Stunning Packaging Design.

We need a new packaging design for our Brand: T&M Hearth & Dwelling. We Manufacture, Market, and Sell Home & Kitchen Products (Such as Kitchen Utensils and Home Decor to name a few) Direct to Consumers in the United States via our Website and Vendaro.com. We would like to see designs that are simple, clean, and modern, yet stand out and demand attention. Our Preferred colors of the design should include: Black or Grey as the base color/shade), White or Grey for the text, and some additional color can be used for complementary elements/visuals at your own discretion or creativity. We would like this to be an Interchangeable Design that can be easily modified and implemented across all of our other products (i.e: does not contain too many images or design elements that reference a particular product.

Although this design and the concept as a whole is intended to be used across our entire catalogue of products. Please feel free to base your design on our one of our top selling products as per the following URL: https://www.vendaro.com/dp/X49QM7713R?ref=myi_title_dp.

Target Market(s)

Our customers tend come from many areas across the spectrum. But the quintessential T&M target customer (the type of person who tends to be our most receptive and loyal customer) is female and part of the Millennials generation, aged in her 30s, and is either working full-time in a white-collar job or on home duties, of which she would have young children, a spouse, or other family members to look after. She’s part of the conventional family life who represent the core of ‘middle America’. She doesn’t mind to splurge every now and again on shopping for items that she wants and/or needs, whilst some of the time she’ll also go out of her way to ‘search for a bargain’. She tends to spend more time in her home and kitchen than the average individual. We recognize that cooking for herself and family, and providing a well furnished and stylish home is part of who she is.

Industry/Entity Type

Retail

Font styles to use
Serif
Sans Serif

Colors

Designer to choose only greyscale colors for use in the design.

Requirements
Must have
• Interchangeable Design (A "Universal" Packaging Design that can be easily modified and adapted for use with a large catalogue of products under our brand).
Nice to have
• Some visual elements that gives our packaging/brand the ability to stand out and be unique/memorable.
Should not have
• Our design should not have too much text. Nor should it be cluttered or overcrowded with too much information or visual elements. And does not contain too many images or design elements that reference a particular product. We believe simplicity is key, and quality over quantity.

```html
<!DOCTYPE html>
<html lang="en">
<head>
<meta charset="utf-8">
<title>T&amp;M Hearth &amp; Dwelling – Pie Server Packaging</title>
<link rel="stylesheet" href="https://fonts.googleapis.com/css2?family=Playfair+Display:wght@400&family=Kalam:wght@400;700&family=Oswald:wght@500&family=Arimo:wght@400&display=swap">
<style>
  :root {
    --panel-dark: #232323;
    --panel-front: #1c1c1b;
    --panel-grey: #555555;
    --ink-white: #ffffff;
    --ink-soft: #e6e6e6;
    --line-grey: #d8d8d8;
    --art-tone-a: #2a2a2a;
    --art-tone-b: #1f1f1f;
  }
  * { margin: 0; padding: 0; box-sizing: border-box; }
  html, body { width: 1015px; height: 1200px; overflow: hidden; background: var(--panel-dark); }
  .package {
    position: relative;
    width: 1015px;
    height: 1200px;
    overflow: hidden;
  }
  .panel { position: absolute; top: 0; height: 1200px; }
  .panel-back { left: 0; width: 346px; background: var(--panel-dark); }
  .panel-side-left { left: 346px; width: 161px; background: var(--panel-grey); }
  .panel-front { left: 507px; width: 347px; background: var(--panel-front); }
  .panel-side-right { left: 854px; width: 161px; background: var(--panel-grey); }

  .brand {
    position: absolute;
    color: var(--ink-white);
    font-family: "Playfair Display", serif;
    font-weight: 400;
    text-align: center;
    line-height: 1.1;
  }
  .brand-main { left: 580px; top: 118px; width: 226px; font-size: 30px; }
  .brand-side { width: 161px; top: 585px; font-size: 20px; }
  .brand-side.left { left: 346px; }
  .brand-side.right { left: 854px; }
  .brand-initials { display: block; font-size: 2.4em; line-height: 1; margin-bottom: 6px; }

  .vertical { position: absolute; writing-mode: vertical-rl; white-space: nowrap; }
  .product-name {
    left: 542px; top: 336px;
    font-family: "Kalam", sans-serif;
    font-weight: 700;
    font-size: 44px;
    letter-spacing: 2px;
    line-height: 1;
    color: var(--ink-white);
  }
  .product-tagline {
    left: 552px; top: 682px;
    font-family: "Kalam", sans-serif;
    font-size: 26px;
    line-height: 1;
    color: var(--ink-white);
  }
  .piece-count {
    left: 788px; top: 823px;
    font-family: "Arimo", sans-serif;
    font-size: 28px;
    letter-spacing: 1px;
    line-height: 1;
    color: var(--ink-soft);
  }

  .product-art {
    position: absolute;
    left: 607px; top: 357px;
    width: 153px; height: 572px;
    border-radius: 76px 76px 20px 20px;
    background: linear-gradient(180deg, var(--art-tone-a), var(--art-tone-b));
  }

  .feature {
    position: absolute;
    top: 1033px;
    width: 86px; height: 86px;
  }
  .feature svg { position: absolute; inset: 0; }
  .feature-label {
    position: absolute; inset: 0;
    display: flex; align-items: center; justify-content: center;
    text-align: center;
    font-family: "Oswald", sans-serif;
    font-weight: 500;
    font-size: 12.5px;
    line-height: 1.45;
    color: var(--ink-white);
  }
  .feature-steel { left: 528px; }
  .feature-edge { left: 638px; }
  .feature-use { left: 747px; }
</style>
</head>
<body>
<main class="package">
  <div class="panel panel-back"></div>
  <div class="panel panel-side-left"></div>
  <div class="panel panel-front"></div>
  <div class="panel panel-side-right"></div>

  <div class="brand brand-main"><span class="brand-initials">T&amp;M</span>Hearth &amp; Dwelling</div>
  <div class="brand brand-side left"><span class="brand-initials">T&amp;M</span>Hearth &amp; Dwelling</div>
  <div class="brand brand-side right"><span class="brand-initials">T&amp;M</span>Hearth &amp; Dwelling</div>

  <h1 class="vertical product-name">PIE SERVER</h1>
  <p class="vertical product-tagline">Cut and serve spatula</p>
  <p class="vertical piece-count">1 PIECE</p>

  <div class="product-art" role="img" aria-label="Line illustration of a serrated pie server with a slotted handle"></div>

  <div class="feature feature-steel">
    <svg viewBox="0 0 86 86" aria-hidden="true">
      <circle cx="43" cy="43" r="41" fill="none" stroke="var(--line-grey)" stroke-width="2.5"/>
      <line x1="4" y1="44" x2="82" y2="44" stroke="var(--line-grey)" stroke-width="1.5"/>
    </svg>
    <div class="feature-label">STAINLESS<br>STEEL</div>
  </div>
  <div class="feature feature-edge">
    <svg viewBox="0 0 86 86" aria-hidden="true">
      <circle cx="43" cy="43" r="41" fill="none" stroke="var(--line-grey)" stroke-width="2.5"/>
      <line x1="4" y1="44" x2="82" y2="44" stroke="var(--line-grey)" stroke-width="1.5"/>
    </svg>
    <div class="feature-label">SERRATED<br>EDGE</div>
  </div>
  <div class="feature feature-use">
    <svg viewBox="0 0 86 86" aria-hidden="true">
      <circle cx="43" cy="43" r="41" fill="none" stroke="var(--line-grey)" stroke-width="2.5"/>
      <line x1="4" y1="44" x2="82" y2="44" stroke="var(--line-grey)" stroke-width="1.5"/>
    </svg>
    <div class="feature-label">PERFECT FOR<br>PIE &amp; CAKE</div>
  </div>
</main>
</body>
</html>
```